Pharmaceutical Manufacturing Services Advertisement

We need a new full page advertisement designed for publication in international magazines. We are a custom pharmaceutical manufacturing company and we help biotechnology companies scale up their drug development for clinical trials. The products we help manufacture are therapeutics for global healthcare problems.

Target Market(s)

Verott Bio is a privately owned contract development manufacturing organisation (CDMO) headquartered in Darra, QLD, Australia.

Our mission is to is to be a global leader in development and in the provision of contract manufacturing for active pharmaceutical ingredient processes.

Why we do what we Do:

To help advance Biotechnology Companies so that they can deliver innovative therapeutics
~ enabling patients to live longer, healthier and happier lives
~ which solves worldwide health problems

Verott Bio’s role is to develop, implement and scale up the production to deliver biologic medicines for patients in partnership with the biotechnology companies.

Industry/Entity Type

Biotechnology

Font styles to use
Sans Serif

Colors

Designer to choose colors to be used in the design.

Requirements
Must have
• Please see the script on the Word document. There are 4 optional Header Taglines. Additional ideas for multiple designs for the taglines welcomed.
• However preference is for either of the first two:
• 1. Building your vision for better healthcare
• 2. Bridging your vision for better healthcare
• File Specs:
• • All artwork should be submitted as high-resolution (300 min. dpi), press-ready PDF files
• • CMYK color only
• • Full page 8.25” x 10.812”; 209.55 x 274.62 mm
• • Live Area for all sizes: 0.25” (6.35 mm) inside the trim
• • Bleed Area for all sizes: Extends 0.125” (3.175 mm) from trim
Nice to have
• Modern Science look to inspire biotechnology companies to work with us.
• Search for images to use by keyword "recombinant dna"

```html
<!DOCTYPE html>
<html lang="en">
<head>
<meta charset="utf-8">
<title>Verott Bio – Building Your Vision for Better Healthcare</title>
<link href="https://fonts.googleapis.com/css2?family=Montserrat:wght@300;400;700;800&display=swap" rel="stylesheet">
<style>
  :root {
    --navy: #02405f;
    --navy-text: #0b3a55;
    --lime: #b3c62b;
    --lime-frame: #c8d72c;
    --slate: #4b5663;
    --ink: #1e1b1c;
    --body: #2d2d2d;
    --mist-top: #e6e7e9;
    --mist-bottom: #f4f5f6;
    --frame: #d3d6da;
    --white: #ffffff;
  }
  * { box-sizing: border-box; margin: 0; padding: 0; }
  html, body { width: 945px; height: 1200px; overflow: hidden; background: var(--white); }
  .ad {
    position: relative;
    width: 945px;
    height: 1200px;
    overflow: hidden;
    font-family: "Montserrat", sans-serif;
    background: var(--white);
  }
  .hero-backdrop {
    position: absolute; left: 0; top: 0;
    width: 945px; height: 456px;
    background: linear-gradient(180deg, var(--mist-top), var(--mist-bottom));
  }
  .hero-rule {
    position: absolute; left: 0; top: 456px;
    width: 945px; height: 6px;
    background: var(--navy);
  }
  .hero-frame {
    position: absolute;
    left: 68px; top: 56px;
    width: 412px; height: 412px;
    border-radius: 50%;
    background: var(--white);
    border: 3px solid var(--frame);
  }
  .hero-photo {
    position: absolute;
    left: 83px; top: 71px;
    width: 382px; height: 382px;
    border-radius: 50%;
    background: radial-gradient(circle at 40% 45%, #e7cbb8 0%, #d9d6d3 45%, #eef0f2 80%, #c9d3dc 100%);
  }
  .headline {
    position: absolute;
    right: 64px;
    top: 94px;
    text-align: right;
    color: var(--navy-text);
    font-weight: 400;
    font-size: 44px;
    line-height: 52px;
    letter-spacing: 0.3px;
  }
  .headline .accent { color: var(--lime); font-weight: 800; font-size: 45px; }
  .subline {
    position: absolute;
    right: 64px;
    top: 324px;
    text-align: right;
    color: var(--slate);
    font-weight: 800;
    font-size: 24px;
    line-height: 30px;
  }
  .intro {
    position: absolute;
    left: 85px;
    top: 553px;
    width: 440px;
    color: var(--body);
    font-weight: 400;
    font-size: 13.8px;
    line-height: 21.6px;
  }
  .intro p + p { margin-top: 21.6px; }
  .offer { position: absolute; left: 590px; width: 300px; }
  .offer--products { top: 531px; }
  .offer--services { top: 671px; }
  .offer__tag {
    display: inline-block;
    background: var(--lime);
    color: var(--white);
    font-weight: 800;
    font-size: 14px;
    line-height: 27px;
    padding: 0 8px;
    margin-bottom: 3px;
  }
  .offer__list { list-style: none; margin-left: -10px; }
  .offer__list li {
    position: relative;
    padding-left: 14px;
    color: var(--ink);
    font-weight: 800;
    font-size: 15px;
    line-height: 23.3px;
  }
  .offer__list li::before {
    content: "";
    position: absolute;
    left: 2px;
    top: 6px;
    width: 4px;
    height: 8px;
    border: solid var(--lime);
    border-width: 0 2px 2px 0;
    transform: rotate(40deg);
  }
  .contact-band {
    position: absolute;
    left: 0;
    top: 873px;
    width: 945px;
    height: 156px;
    background: var(--navy);
  }
  .contact {
    position: absolute;
    left: 560px;
    top: 893px;
    color: var(--white);
    font-size: 17px;
    line-height: 26.6px;
    font-style: normal;
  }
  .contact__label { font-weight: 300; }
  .contact__row { display: flex; align-items: center; gap: 7px; }
  .contact__row svg { flex: none; }
  .contact__row--bold { font-weight: 800; }
  .contact__row--light { font-weight: 300; }
  .gallery__tile {
    position: absolute;
    width: 208px;
    height: 151px;
    border: 4px solid var(--lime-frame);
    border-radius: 16px;
    overflow: hidden;
  }
  .tile-a { left: 84px; top: 829px; background: linear-gradient(135deg, #e9eaec 0%, #a6a9ad 45%, #3e4650 75%, #21324f 100%); }
  .tile-b { left: 324px; top: 829px; background: linear-gradient(135deg, #f3f5f7 0%, #dfe4ea 55%, #9fb3d4 80%, #eef1f4 100%); }
  .tile-c { left: 84px; top: 1006px; background: linear-gradient(120deg, #f4dccb 0%, #f3e9e3 50%, #fafafa 100%); }
  .tile-d { left: 324px; top: 1006px; background: radial-gradient(circle at 55% 55%, #7fb9c8 0%, #2f7e92 45%, #0c3440 100%); }
  .brand {
    position: absolute;
    left: 578px;
    top: 1086px;
  }
  .brand__row { display: flex; align-items: center; gap: 10px; }
  .brand__name {
    color: var(--navy);
    font-weight: 800;
    font-size: 36px;
    line-height: 42px;
    letter-spacing: 0.5px;
  }
  .brand__dot {
    width: 20px; height: 20px;
    border-radius: 50%;
    background: var(--lime-frame);
  }
  .brand__descriptor {
    margin-top: 2px;
    color: var(--slate);
    font-weight: 400;
    font-size: 11px;
    letter-spacing: 0.2px;
  }
</style>
</head>
<body>
<main class="ad">
  <div class="hero-backdrop"></div>
  <div class="hero-rule"></div>
  <div class="hero-frame"></div>
  <div class="hero-photo" role="img" aria-label="Photo: scientist in safety glasses cutting a strand of DNA with scissors"></div>

  <h1 class="headline">
    BUILDING<br>YOUR VISION<br>FOR <span class="accent">BETTER</span><br><span class="accent">HEALTHCARE</span>
  </h1>
  <p class="subline">Your Partner in<br>Early Phase Clinical<br>Biomanufacturing</p>

  <section class="intro">
    <p>We have been serving the pharmaceutical, biotechnology and veterinary industry for over 20 years so you can create innovative medicines for worldwide health problems.</p>
    <p>Get your therapeutics to the patient faster with cost-effective manufacturing for your GMP clinical trial material. We offer rapid technology transfer, scale-up development and manufacturing of microbial cell-derived proteins at up to 500L scale. We prepare your active pharmaceutical ingredient (API) products to a world class standard ready for clinical development.</p>
  </section>

  <section class="offer offer--products">
    <span class="offer__tag">PRODUCTS</span>
    <ul class="offer__list">
      <li>Recombinant proteins</li>
      <li>Live Biotherapeutics</li>
      <li>Bacterial vaccines</li>
      <li>Plasmid DNA</li>
    </ul>
  </section>

  <section class="offer offer--services">
    <span class="offer__tag">SERVICES</span>
    <ul class="offer__list">
      <li>Bacterial / Yeast Fermentation</li>
      <li>Cell Banking</li>
      <li>Process Development/Scale-up</li>
      <li>cGMP Manufacture of<br>biopharmaceutical APIs</li>
      <li>Stability Testing</li>
    </ul>
  </section>

  <div class="contact-band"></div>

  <div class="gallery">
    <div class="gallery__tile tile-a" role="img" aria-label="Photo: stainless steel bioreactor with control panel"></div>
    <div class="gallery__tile tile-b" role="img" aria-label="Photo: gloved hands working with petri dishes and vials on a lab bench"></div>
    <div class="gallery__tile tile-c" role="img" aria-label="Photo: child receiving a vaccine injection in the arm"></div>
    <div class="gallery__tile tile-d" role="img" aria-label="Photo: pipette tips over a culture dish in blue light"></div>
  </div>

  <address class="contact">
    <div class="contact__label">Visit</div>
    <div class="contact__row contact__row--bold">
      <svg width="15" height="15" viewBox="0 0 14 14" fill="none" stroke="#b3c62b" stroke-width="1.3"><circle cx="7" cy="7" r="6"/><ellipse cx="7" cy="7" rx="2.6" ry="6"/><path d="M1 7h12M2 4h10M2 10h10"/></svg>
      verottbio.com.au
    </div>
    <div class="contact__row contact__row--bold">
      <svg width="15" height="15" viewBox="0 0 14 14"><rect x="0" y="0" width="14" height="14" rx="2" fill="#b3c62b"/><path d="M4 3c-1 1-1 3 1 5s4 2.5 5 1.5l-1.5-1.5-1 .6c-.8-.4-1.8-1.4-2.2-2.2l.6-1L4.4 3z" fill="#02405f"/></svg>
      Australia +61(7)30000418
    </div>
    <div class="contact__row contact__row--light">
      <svg width="15" height="13" viewBox="0 0 14 12" fill="none" stroke="#b3c62b" stroke-width="1.3"><rect x="0.7" y="0.7" width="12.6" height="10.6"/><path d="M0.7 0.7L7 6.5l6.3-5.8"/></svg>
      enquiries@verottbio.com.au
    </div>
  </address>

  <div class="brand">
    <div class="brand__row">
      <span class="brand__name">VEROTT BIO</span>
      <span class="brand__dot"></span>
    </div>
    <div class="brand__descriptor">BIOPHARMACEUTICAL MANUFACTURING</div>
  </div>
</main>
</body>
</html>
```